Postcard flyer for body postive dance classes

We need an eye catching double sided A6 postcard for body positive dance classes. The business name is stepbloomjoy and already have a rough logo and some text that needs tidying up and putting together. The design needs to be simple and elegant. We are appealing to a diverse range of adult women with or without dance experience to join us in a safe, supportive and creative environment. We would like the design to use black, white and a soft green. The final design should communicate movement, contentment and wholeness. File with information attached.

Target Market(s)

Diverse range of adult women

Industry/Entity Type

Health And Wellness

Font styles to use
Other font styles liked:
• Candara or similar but open to suggestions

Colors
abd036
cadf82
eaf2ce
fffefb
fef9ed
fff3d1
ffffff

Requirements
Must have
• Logo and text provided.
Nice to have
• Sense of movement. Match to website colours and style.
Should not have
• Intimidating perfect body images

```html
<!DOCTYPE html>
<html lang="en">
<head>
<meta charset="utf-8">
<title>stepbloomjoy – Flow With Life</title>
<link rel="stylesheet" href="https://fonts.googleapis.com/css2?family=Oswald:wght@300;400;500&display=swap">
<style>
  :root {
    --bg-light: #8a8a8a;
    --bg-mid: #5f5f5f;
    --bg-dark: #3b3b3b;
    --ink: #ffffff;
    --green-strong: #abd036;
    --green-soft: #cadf82;
    --green-pale: #eaf2ce;
    --cream: #fffefb;
    --url-tone: #cadf82;
  }
  * { margin: 0; padding: 0; box-sizing: border-box; }
  html, body {
    width: 1200px;
    height: 851px;
    overflow: hidden;
    background: var(--bg-dark);
  }
  .postcard {
    position: relative;
    width: 1200px;
    height: 851px;
    overflow: hidden;
    background: linear-gradient(100deg, var(--bg-light) 0%, var(--bg-mid) 45%, var(--bg-dark) 100%);
    font-family: "Oswald", "Arial Narrow", sans-serif;
    color: var(--ink);
  }
  .dancer-photo {
    position: absolute;
    left: 10px;
    top: 64px;
    width: 380px;
    height: 768px;
    border-radius: 28px;
    background:
      radial-gradient(ellipse 70% 45% at 55% 35%, var(--cream) 0%, rgba(255,254,251,0) 100%),
      linear-gradient(170deg, var(--green-pale) 0%, #d9dccf 45%, #b9bcb1 100%);
    box-shadow: 0 0 40px 10px rgba(255, 255, 255, 0.35);
  }
  .headline {
    position: absolute;
    right: 60px;
    line-height: 1;
    text-align: right;
    white-space: nowrap;
  }
  .headline--flow { top: 59px; font-size: 118px; font-weight: 300; letter-spacing: 9px; margin-right: -9px; }
  .headline--life { top: 184px; font-size: 311px; font-weight: 400; }
  .tagline {
    position: absolute;
    right: 60px;
    font-size: 57px;
    line-height: 1;
    font-weight: 400;
    letter-spacing: 4px;
    margin-right: -4px;
    text-align: right;
    white-space: nowrap;
  }
  .tagline--first { top: 550px; }
  .tagline--second { top: 648px; }
  .brand {
    position: absolute;
    left: 404px;
    top: 676px;
    display: flex;
    align-items: center;
    gap: 10px;
  }
  .brand-dot {
    width: 22px;
    height: 22px;
    border-radius: 50%;
    background: var(--green-strong);
  }
  .brand-name {
    font-size: 30px;
    line-height: 1;
    font-weight: 400;
    color: var(--green-soft);
    white-space: nowrap;
  }
  .web-address {
    position: absolute;
    right: 56px;
    top: 763px;
    font-size: 46px;
    line-height: 1;
    font-weight: 500;
    color: var(--url-tone);
    letter-spacing: 1px;
    white-space: nowrap;
  }
</style>
</head>
<body>
  <main class="postcard">
    <div class="dancer-photo" role="img" aria-label="Photograph of a dancer in a flowing white dress arching backwards on pointe, softly glowing against the grey background"></div>

    <h1>
      <span class="headline headline--flow">FLOW WITH</span>
      <span class="headline headline--life">LIFE</span>
    </h1>

    <p>
      <span class="tagline tagline--first">THROUGH YOUR INNER</span>
      <span class="tagline tagline--second">DANCER</span>
    </p>

    <div class="brand">
      <span class="brand-dot"></span>
      <span class="brand-name">stepbloomjoy</span>
    </div>

    <p class="web-address">WWW.STEPBLOOMJOY.COM.AU</p>
  </main>
</body>
</html>
```